Silver Lantern Restaurant
Silver Lantern Restaurant Stationery - Food
Silver Lantern Restaurant Stationery
Modern
Khalid Bazzour
CEO
Phone: 012 7318465 012 7352941 487 Jeddah 21833 Rawdah St. North from Jeddah Harbor Plaza
info@silverlantern-dining.example
www.silverlantern-dining.example
Requirements: 1. Business card 2. Letterhead 3. Envelope (DL only) check attached image 4. Notepad 5. cake box - check attached image 6. Cardboard Paper Bag
Design
rimasoufek rimasoufek
Thanks to everyone really nice work, but please don't submit business card solo, I don't need all stationery i need only what's mentioned in additional comments section in the brief.

```html
<!DOCTYPE html>
<html lang="en">
<head>
<meta charset="utf-8">
<title>Silver Lantern Restaurant – Business Card</title>
<link rel="stylesheet" href="https://fonts.googleapis.com/css2?family=Open+Sans:wght@400;600&display=swap">
<style>
  :root {
    --backdrop: #8e8f8f;
    --gold-light: #f6b044;
    --gold-mid: #e0901c;
    --gold-deep: #a8610c;
    --charcoal: #3d3d3b;
    --paper: #ffffff;
    --ink: #4a4a4a;
    --badge: #f3ead9;
  }
  * { box-sizing: border-box; margin: 0; padding: 0; }
  html, body { width: 1200px; height: 908px; overflow: hidden; }
  body {
    background: var(--backdrop);
    font-family: "Open Sans", sans-serif;
    position: relative;
  }
  .card {
    position: absolute;
    top: 299px;
    width: 540px;
    height: 310px;
    border-radius: 16px;
    overflow: hidden;
    box-shadow: 0 12px 28px rgba(0,0,0,.35);
  }
  .card--front {
    left: 40px;
    background: linear-gradient(135deg, var(--gold-deep) 0%, var(--gold-mid) 45%, var(--gold-light) 100%);
  }
  .card--back { left: 620px; background: var(--paper); }

  .brand {
    position: absolute;
    display: flex;
    flex-direction: column;
    align-items: center;
  }
  .brand__mark { border-radius: 50%; background: var(--badge); }
  .brand__name { font-weight: 600; white-space: nowrap; }

  .card--front .brand { left: 170px; top: 70px; width: 200px; }
  .card--front .brand__mark { width: 126px; height: 126px; }
  .card--front .brand__name { color: var(--paper); font-size: 22px; margin-top: 12px; }

  .card__bands { position: absolute; inset: 0; }

  .card--back .brand { left: 28px; top: 26px; width: 130px; }
  .card--back .brand__mark { width: 70px; height: 70px; background: var(--gold-light); }
  .card--back .brand__name { color: var(--gold-mid); font-size: 15px; margin-top: 6px; }

  .contact {
    position: absolute;
    left: 30px;
    top: 140px;
    width: 260px;
    list-style: none;
    color: var(--ink);
    font-size: 12px;
    line-height: 1.45;
  }
  .contact__item { display: flex; align-items: flex-start; gap: 7px; margin-bottom: 3px; }
  .contact__icon { flex: none; margin-top: 2px; }

  .person {
    position: absolute;
    right: 18px;
    top: 140px;
    width: 120px;
    text-align: right;
    color: var(--paper);
  }
  .person__name { font-size: 15px; font-weight: 600; white-space: nowrap; }
  .person__role { font-size: 11px; letter-spacing: 1px; margin-top: 2px; }
</style>
</head>
<body>

<section class="card card--front" aria-label="Business card front">
  <div class="brand">
    <div class="brand__mark"></div>
    <p class="brand__name">Silver Lantern</p>
  </div>
</section>

<section class="card card--back" aria-label="Business card back">
  <svg class="card__bands" width="540" height="310" viewBox="0 0 540 310">
    <defs>
      <linearGradient id="goldBand" x1="0" y1="0" x2="1" y2="1">
        <stop offset="0" stop-color="#f6b044"/>
        <stop offset="1" stop-color="#c97712"/>
      </linearGradient>
    </defs>
    <path d="M220 0 H300 C360 90 390 200 400 310 H340 C330 200 290 80 220 0 Z" fill="#3d3d3b"/>
    <path d="M300 0 H540 V310 H400 C390 200 360 90 300 0 Z" fill="url(#goldBand)"/>
  </svg>

  <div class="brand">
    <div class="brand__mark"></div>
    <p class="brand__name">Silver Lantern</p>
  </div>

  <ul class="contact">
    <li class="contact__item">
      <svg class="contact__icon" width="11" height="11" viewBox="0 0 12 12"><circle cx="6" cy="6" r="6" fill="#e0901c"/><path d="M4 3.2l1 1.4-.6.8c.4.9 1.1 1.6 2 2l.8-.6 1.4 1-.6 1c-2.6-.2-4.5-2.1-4.7-4.7z" fill="#fff"/></svg>
      <span>012 7318465</span>
    </li>
    <li class="contact__item">
      <svg class="contact__icon" width="11" height="11" viewBox="0 0 12 12"><circle cx="6" cy="6" r="6" fill="#e0901c"/><path d="M4 3.2l1 1.4-.6.8c.4.9 1.1 1.6 2 2l.8-.6 1.4 1-.6 1c-2.6-.2-4.5-2.1-4.7-4.7z" fill="#fff"/></svg>
      <span>012 7352941</span>
    </li>
    <li class="contact__item">
      <svg class="contact__icon" width="11" height="11" viewBox="0 0 12 12"><circle cx="6" cy="6" r="6" fill="#e0901c"/><path d="M6 2.5a2.2 2.2 0 0 1 2.2 2.2C8.2 6.4 6 9.3 6 9.3S3.8 6.4 3.8 4.7A2.2 2.2 0 0 1 6 2.5z" fill="#fff"/></svg>
      <span>487 Jeddah 21833<br>Rawdah St.<br>North from Jeddah Harbor Plaza</span>
    </li>
    <li class="contact__item">
      <svg class="contact__icon" width="11" height="11" viewBox="0 0 12 12"><circle cx="6" cy="6" r="6" fill="#e0901c"/><rect x="3" y="4" width="6" height="4.2" fill="#fff"/><path d="M3 4l3 2.3L9 4" stroke="#e0901c" stroke-width=".7" fill="none"/></svg>
      <span>info@silverlantern-dining.example</span>
    </li>
    <li class="contact__item">
      <svg class="contact__icon" width="11" height="11" viewBox="0 0 12 12"><circle cx="6" cy="6" r="6" fill="#e0901c"/><circle cx="6" cy="6" r="3" stroke="#fff" stroke-width=".8" fill="none"/><path d="M3 6h6M6 3v6" stroke="#fff" stroke-width=".7"/></svg>
      <span>www.silverlantern-dining.example</span>
    </li>
  </ul>

  <div class="person">
    <p class="person__name">Khalid Bazzour</p>
    <p class="person__role">CEO</p>
  </div>
</section>

</body>
</html>
```